Re-branding stationary for Company

Orvane Diamonds is a diamond trading company that has been established since more then 30years.

We are currently looking to re-design our current logo design into something more modern and more appealing the the new generation. Small changes are what we are looking for that will give our company a little more modern look and a new appeal.
The design should be on similar lines to what our current logo is, but we are definitely wanting to have some modern changes to this.
Along with this, we are looking to have design for complete stationary including, business cards, envelopes, letterheads, etc..

Attached is our current logo, can use this as a base point towards creating a new design.
Updates

Project Deadline Extended Reason: Am still looking for wonderful and amazingly creative design for my company, a facelift with a little modern touchHave provided you with a current logo of the company as inspiration to make something new and unique. PLEASE DO NOT USE COPY THE LOGO FILE AS IT IS! Added Wednesday, May 6, 2015

Target Market(s)

We are a company established since over 30 years, and want to maintain our core fundamental values which is portrayed through our logo. Use this as a base into creating new modern design.

Industry/Entity Type

It Company

Font styles to use
Serif
Sans Serif
Decorative
Script

Requirements
Must have
• A modern touch
• Color combination should be similar in terms with what we currently use in attached design.
Nice to have
• Want that the design is appealing using simple but yet modern features to change and restructure the current company logo.
Should not have
• Not looking more multi colored design
• Not gotta be too overly extravagant

```html
<!DOCTYPE html>
<html lang="en">
<head>
<meta charset="utf-8">
<title>Orvane Diamonds – Stationery Set</title>
<link href="https://fonts.googleapis.com/css2?family=Arimo:wght@400;700&display=swap" rel="stylesheet">
<style>
  :root {
    --navy: #0d2460;
    --paper: #f2f2f2;
    --backdrop: #bababa;
    --faint: #d2d5dc;
    --faint-on-navy: #3a4d80;
    --ink: #3a3a3a;
  }
  * { margin: 0; padding: 0; box-sizing: border-box; }
  html, body { width: 1200px; height: 900px; overflow: hidden; }
  body {
    position: relative;
    background: var(--backdrop);
    font-family: "Arimo", Arial, sans-serif;
    color: var(--ink);
  }
  .sheet { position: absolute; background: var(--paper); overflow: hidden; }
  .band { position: absolute; top: 0; bottom: 0; background: var(--navy); }
  .wordmark {
    position: absolute; z-index: 1;
    display: flex; align-items: center; gap: 4px;
    font-weight: 700; color: var(--navy); white-space: nowrap;
  }
  .wordmark .mark-square { background: var(--navy); flex: none; }
  .wordmark.on-navy { color: var(--paper); }
  .wordmark.on-navy .mark-square { background: var(--paper); }
  .motif { position: absolute; z-index: 0; border-radius: 50%; background: var(--faint); }
  .contact { position: absolute; z-index: 1; font-size: 6.5px; line-height: 1.3; color: var(--ink); white-space: nowrap; }

  /* letterhead */
  .letterhead { left: 240px; top: 100px; width: 350px; height: 457px; }
  .letterhead .band-wide { left: 0; width: 14px; }
  .letterhead .band-thin { left: 17px; width: 2px; }
  .letterhead .wordmark { left: 30px; top: 28px; font-size: 12px; }
  .letterhead .mark-square { width: 22px; height: 22px; }
  .letterhead .motif { right: 10px; bottom: 18px; width: 80px; height: 80px; }
  .letterhead .address { left: 39px; bottom: 10px; }
  .letterhead .reach { left: 158px; bottom: 16px; }

  /* business card front */
  .card-front { left: 616px; top: 108px; width: 146px; height: 82px; }
  .card-front .band-wide { left: 0; width: 76px; }
  .card-front .band-thin { left: 78px; width: 2px; }
  .card-front .wordmark { left: 8px; top: 38px; font-size: 6.5px; }
  .card-front .mark-square { width: 10px; height: 10px; }
  .card-front .motif { right: 4px; bottom: 6px; width: 30px; height: 30px; }

  /* business card back */
  .card-back { left: 616px; top: 214px; width: 146px; height: 83px; }
  .card-back .band-wide { left: 0; width: 6px; }
  .card-back .band-thin { left: 8px; width: 1px; }
  .card-back .wordmark { left: 16px; top: 16px; font-size: 6.5px; }
  .card-back .mark-square { width: 10px; height: 10px; }
  .card-back .motif { right: 3px; bottom: 3px; width: 18px; height: 18px; }
  .card-back .contact { font-size: 4.5px; }
  .card-back .address { left: 18px; top: 52px; }
  .card-back .person { left: 96px; top: 15px; }
  .card-back .reach { left: 96px; top: 50px; }

  /* phone screen */
  .screen {
    left: 810px; top: 143px; width: 95px; height: 140px;
    background: linear-gradient(160deg, #1a3478, var(--navy) 70%);
  }
  .screen .wordmark { left: 8px; top: 22px; font-size: 6px; }
  .screen .mark-square { width: 8px; height: 8px; }
  .screen .motif { right: 4px; bottom: 2px; width: 38px; height: 38px; background: var(--faint-on-navy); }

  /* envelope */
  .envelope { left: 663px; top: 403px; width: 360px; height: 181px; }
  .envelope .band-wide { left: 0; width: 12px; }
  .envelope .band-thin { left: 15px; width: 2px; }
  .envelope .wordmark { left: 27px; top: 38px; font-size: 11px; }
  .envelope .mark-square { width: 20px; height: 20px; }
  .envelope .motif { right: 10px; bottom: 18px; width: 62px; height: 62px; }
  .envelope .address { left: 27px; bottom: 6px; }
  .envelope .reach { left: 133px; bottom: 12px; }

  /* cd sleeve */
  .sleeve { left: 325px; top: 627px; width: 202px; height: 203px; background: var(--navy); }
  .sleeve .wordmark { left: 53px; top: 32px; font-size: 7.5px; }
  .sleeve .mark-square { width: 14px; height: 14px; }
  .sleeve .motif { right: 8px; bottom: 10px; width: 60px; height: 60px; background: var(--faint-on-navy); }

  /* cd disc */
  .disc { position: absolute; left: 670px; top: 627px; width: 180px; height: 191px; }
  .disc .wordmark { left: 5px; top: 72px; font-size: 6px; gap: 3px; }
  .disc .mark-square { width: 9px; height: 9px; }
</style>
</head>
<body>

<section class="sheet letterhead" aria-label="Letterhead">
  <div class="band band-wide"></div>
  <div class="band band-thin"></div>
  <div class="wordmark"><span class="name">Orvane Diamonds</span><span class="mark-square"></span></div>
  <div class="motif"></div>
  <p class="contact address">Orvane Diamonds<br>#42, Varun Lane, R.S. Nagar,<br>Pune- 411 020</p>
  <p class="contact reach">P: 020 5512 7789<br>E: info@orvanediamonds.com</p>
</section>

<section class="sheet card-front" aria-label="Business card front">
  <div class="band band-wide"></div>
  <div class="band band-thin"></div>
  <div class="wordmark on-navy"><span class="name">Orvane Diamonds</span><span class="mark-square"></span></div>
  <div class="motif"></div>
</section>

<section class="sheet card-back" aria-label="Business card back">
  <div class="band band-wide"></div>
  <div class="band band-thin"></div>
  <div class="motif"></div>
  <div class="wordmark"><span class="name">Orvane Diamonds</span><span class="mark-square"></span></div>
  <p class="contact person">DEV MALHAR<br>CEO</p>
  <p class="contact address">#42, Varun Lane, R.S. Nagar,<br>Pune- 411 020<br>P: 020 5512 7789<br>E: info@orvanediamonds.com</p>
  <p class="contact reach">+91 98110 42375<br>devmalhar@mail.com</p>
</section>

<section class="sheet screen" aria-label="Mobile screen">
  <div class="wordmark on-navy"><span class="name">Orvane Diamonds</span><span class="mark-square"></span></div>
  <div class="motif"></div>
</section>

<section class="sheet envelope" aria-label="Envelope">
  <div class="band band-wide"></div>
  <div class="band band-thin"></div>
  <div class="wordmark"><span class="name">Orvane Diamonds</span><span class="mark-square"></span></div>
  <div class="motif"></div>
  <p class="contact address">Orvane Diamonds<br>#42, Varun Lane, R.S. Nagar,<br>Pune- 411 020</p>
  <p class="contact reach">P: 020 5512 7789<br>E: info@orvanediamonds.com</p>
</section>

<section class="sheet sleeve" aria-label="CD sleeve">
  <div class="wordmark on-navy"><span class="name">Orvane Diamonds</span><span class="mark-square"></span></div>
  <div class="motif"></div>
</section>

<section class="disc" aria-label="CD disc">
  <svg width="180" height="191" viewBox="0 0 180 191">
    <defs>
      <clipPath id="disc-shape"><circle cx="90" cy="95" r="90"/></clipPath>
    </defs>
    <g clip-path="url(#disc-shape)">
      <rect x="0" y="0" width="180" height="191" fill="var(--paper)"/>
      <rect x="0" y="0" width="82" height="191" fill="var(--navy)"/>
      <rect x="85" y="0" width="7" height="191" fill="var(--navy)"/>
      <circle cx="128" cy="130" r="28" fill="var(--faint)"/>
    </g>
    <circle cx="90" cy="95" r="22" fill="#ffffff" fill-opacity="0.35"/>
    <circle cx="90" cy="95" r="11" fill="var(--backdrop)"/>
  </svg>
  <div class="wordmark on-navy"><span class="name">Orvane Diamonds</span><span class="mark-square"></span></div>
</section>

</body>
</html>
```